New flavour! New packaging for Velocity Energy Drink!

We need a new packaging designed to show off our new grape flavored energy drink! It will require box design with matching sachets!

Established in 2018 we are a fully Australian owned and operated business that started out with 2 gamers that got sick and tired of sugary energy drinks OR expensive powder from the USA.

We are an energy drink in the esports and gaming space. Our new product is an energy drink in powder in boxes of 30 sachets (please see attached for product example)

Please see example 1 and 2 for our competitors product. We would ideally like to go a bit more minimalist than them but still have a great color pop on black backing.

Target Market(s)

Gamer's and esports athletes between the ages or 18-30

Font styles to use
Sans Serif
Other font styles liked:
• Helvetica

Colors
886aae
ffffff

Requirements
Must have
• Black base/background.
• Vibrant purple N in the Velocity Logo.
• Same or slightly different shades of purple for some text and highlights.
• Black, white and some shades of a vibrant purple (for the grape flavor)
• ingredients list (may need to be reformatted to suit)
• Please see attached for legislative requirements on the box and sachets.
Nice to have
• minimalist design but enough to be eye catching and somewhat playful
• Twitter: @VLCT_FUEL
• Instagram: @VLCT_FUEL
• Facebook: @VLCTFUEL
Should not have
• OTHER COLORS.
• Overly complex designs.

```html
<!DOCTYPE html>
<html lang="en">
<head>
<meta charset="UTF-8">
<title>Velocity Energy Drink – Grape Flavour Box</title>
<link href="https://fonts.googleapis.com/css2?family=Montserrat:wght@300;500;600;700;800&display=swap" rel="stylesheet">
<style>
  :root {
    --page: #f7f7f8;
    --box-black: #232323;
    --side-black: #1a1a1a;
    --grape-pink: #d531ea;
    --grape-violet: #7b2cb3;
    --white: #ffffff;
  }
  * { margin: 0; padding: 0; box-sizing: border-box; }
  html, body {
    width: 1200px;
    height: 845px;
    overflow: hidden;
    background: var(--page);
    font-family: "Montserrat", Helvetica, Arial, sans-serif;
  }
  .box-side {
    position: absolute;
    left: 336px;
    top: 42px;
    width: 72px;
    height: 760px;
    background: var(--side-black);
    overflow: hidden;
  }
  .side-brand {
    position: absolute;
    left: 10px;
    top: 40px;
    height: 420px;
    writing-mode: vertical-rl;
    transform: rotate(180deg);
    display: flex;
    align-items: center;
    justify-content: flex-start;
    gap: 12px;
    color: var(--white);
    font-weight: 800;
    font-size: 46px;
    letter-spacing: 1px;
    line-height: 1;
    text-transform: uppercase;
    white-space: nowrap;
  }
  .box-front {
    position: absolute;
    left: 408px;
    top: 42px;
    width: 448px;
    height: 760px;
    background: var(--box-black);
    overflow: hidden;
  }
  .brand {
    position: absolute;
    left: 0;
    right: 0;
    top: 42px;
    display: flex;
    align-items: center;
    justify-content: center;
    gap: 12px;
    color: var(--white);
    font-weight: 800;
    font-size: 44px;
    letter-spacing: 1px;
    text-transform: uppercase;
  }
  .brand-mark {
    width: 14px;
    height: 14px;
    background: var(--grape-pink);
  }
  .grape-art {
    position: absolute;
    left: 0;
    top: 132px;
    width: 250px;
    height: 560px;
    background: linear-gradient(160deg, var(--grape-pink) 0%, var(--grape-violet) 100%);
    opacity: 0.85;
    border-radius: 0 120px 120px 0;
  }
  .claim {
    position: absolute;
    top: 130px;
    height: 388px;
    writing-mode: vertical-rl;
    transform: rotate(180deg);
    text-align: start;
    white-space: nowrap;
    line-height: 1;
  }
  .claim-product {
    left: 286px;
    font-size: 42px;
    font-weight: 600;
    color: var(--white);
  }
  .claim-flavour {
    left: 338px;
    font-size: 42px;
    font-weight: 600;
    color: var(--white);
  }
  .claim-ingredients {
    left: 380px;
    font-size: 23px;
    font-weight: 300;
    color: var(--white);
  }
  .accent { color: var(--grape-pink); }
  .divider {
    position: absolute;
    left: 327px;
    top: 128px;
    width: 2px;
    height: 410px;
    background: var(--grape-pink);
  }
  .serves-badge {
    position: absolute;
    left: 280px;
    top: 534px;
    width: 126px;
    height: 130px;
    border-radius: 16px;
    background: var(--grape-pink);
    color: var(--box-black);
    display: flex;
    flex-direction: column;
    align-items: center;
    justify-content: center;
    line-height: 1;
  }
  .serves-count { font-size: 54px; font-weight: 600; }
  .serves-label { font-size: 24px; font-weight: 500; margin-top: 2px; }
  .tagline {
    position: absolute;
    left: 48px;
    top: 648px;
    width: 214px;
    color: var(--white);
    font-size: 14px;
    font-weight: 500;
    padding-bottom: 5px;
    border-bottom: 2px solid var(--grape-pink);
    white-space: nowrap;
  }
</style>
</head>
<body>
  <aside class="box-side">
    <div class="side-brand"><span class="side-brand-name">Velocity</span><span class="brand-mark"></span></div>
  </aside>

  <main class="box-front">
    <div class="brand"><span class="brand-name">Velocity</span><span class="brand-mark"></span></div>

    <div class="grape-art" role="img" aria-label="Outline illustration of a grape bunch with leaf and curling vine in pink-to-violet gradient"></div>

    <div class="divider"></div>
    <div class="claim claim-product"><span class="accent">ENERGY</span>&nbsp; DRINK</div>
    <div class="claim claim-flavour">GRAPE <span class="accent">FLAVOUR</span></div>
    <div class="claim claim-ingredients">With Ginseng &amp; Caffeine</div>

    <div class="serves-badge">
      <span class="serves-count">30</span>
      <span class="serves-label">serves</span>
    </div>

    <p class="tagline">FOR GAMERS, BY GAMERS</p>
  </main>
</body>
</html>
```